'Macro at Hand' flyer design.

We need a flyer design for a new company called 'Macro at hand'. We deliver high protein, frozen meals to people in their homes. Mainly aiming at the fitness community. The flyer size will be DL (210mm x 99mm).

We already have a logo as attached below, and would obviously like it to be on the flyer somewhere. We would also like the overall design of the flyer to be in line with the logo (so that the design of the flyer works with the logo and does not contrast it too much).

If you are using any visuals (pictures, background pictures etc.) please do not reference it to any food. Rather we prefer if you used fitness as your inspiration. Please see the picture of Bertil attached for guide. If you are stuck for ideas you can use this photo, however drawn in art. Any pictures you do use please ensure that you have copyright privileges to.

Be as creative as you like with the flyer design. The logo has limited colors however we do not want the flyer to look boring!

These texts will be included on the flyer in the exact order as follows:

- Live a busy lifestyle? No time to meal prep? We do it for you!

- Whether you're bodybuilding or just want truly healthy meals, order from us online.

- Grab and Go meals that you can take to work, school...anywhere.

- High protein, low fat, low sodium.

- No artificial flavours, colours or preservatives.

- Delivered straight to your door, on the day of your choice^.

- Affordable prices.

Remember, if you fail to plan then you plan to fail.

Visit us at www.macroathand.com.au

^Please visit website for conditions.

Target Market(s)

Fitness community.

Industry/Entity Type

Fitness

Requirements
Must have
• Overall design must work with logo.
Nice to have
• Colors.
Should not have
• Any pictures in reference to food.

```html
<!DOCTYPE html>
<html lang="en">
<head>
<meta charset="utf-8">
<title>Macro at Hand – DL Flyer</title>
<link rel="stylesheet" href="https://fonts.googleapis.com/css2?family=Oswald:wght@500;600;700&display=swap">
<style>
  :root {
    --backdrop: #3d3d3d;
    --paper: #ffffff;
    --brand-red: #b81e3a;
    --wedge-black: #0d0d0d;
    --card-pink: #ebbdc5;
    --ink: #2b1a1d;
    --muted: #6b6b6b;
    --photo-dark: #2e2e2e;
    --photo-light: #9a9a9a;
  }
  * { box-sizing: border-box; margin: 0; padding: 0; }
  html, body {
    width: 1200px; height: 1000px; overflow: hidden;
    background: var(--backdrop);
    font-family: "Oswald", "Arial Narrow", sans-serif;
  }
  .flyer {
    position: absolute; left: 78px; top: 255px;
    width: 1045px; height: 491px;
    background: var(--paper);
    border: 1px solid #000;
    overflow: hidden;
  }
  .flyer__panels { position: absolute; inset: 0; }

  .brand {
    position: absolute; left: 0; top: 0; width: 355px; height: 128px;
    display: flex; align-items: center; justify-content: center; gap: 12px;
  }
  .brand__mark { width: 22px; height: 22px; background: var(--brand-red); }
  .brand__name {
    font-size: 40px; font-weight: 700; color: var(--brand-red);
    text-transform: uppercase; letter-spacing: 0.5px;
  }

  .hero-photo {
    position: absolute; left: 0; top: 128px; width: 355px; height: 197px;
    background: linear-gradient(180deg, var(--photo-dark) 0%, #5a5a5a 55%, var(--photo-light) 100%);
  }

  .motto {
    position: absolute; left: 0; top: 285px; width: 400px;
    text-align: center; color: var(--brand-red);
    font-size: 19px; font-weight: 700; line-height: 26px; text-transform: uppercase;
  }

  .visit {
    position: absolute; left: 0; top: 380px; width: 360px; text-align: center;
  }
  .visit__lead { color: var(--muted); font-size: 19px; font-weight: 600; }
  .visit__url { color: var(--brand-red); font-size: 25px; font-weight: 700; line-height: 34px; }
  .visit__note { color: var(--muted); font-size: 16px; font-weight: 600; }

  .benefits { position: absolute; inset: 0; list-style: none; }
  .benefit {
    position: absolute; right: 40px;
    background: var(--card-pink);
    box-shadow: 2px 3px 3px rgba(0,0,0,0.35);
    color: var(--ink); font-size: 22px; font-weight: 600; line-height: 28px;
    padding: 6px 10px 6px 6px;
  }
  .benefit span { display: block; padding-left: 16px; }
  .benefit--1 { left: 350px; top: 25px; height: 43px; }
  .benefit--2 { left: 362px; top: 78px; height: 68px; padding-left: 15px; }
  .benefit--3 { left: 377px; top: 157px; height: 68px; padding-left: 16px; }
  .benefit--4 { left: 392px; top: 236px; height: 43px; padding-left: 24px; }
  .benefit--5 { left: 407px; top: 290px; height: 44px; padding-left: 22px; }
  .benefit--6 { left: 422px; top: 345px; height: 67px; padding-left: 18px; }
  .benefit--7 { left: 437px; top: 424px; height: 42px; padding-left: 29px; }
</style>
</head>
<body>
<main class="flyer">
  <svg class="flyer__panels" width="1045" height="491" viewBox="0 0 1045 491" aria-hidden="true">
    <polygon points="337,0 1045,0 1045,491 442,491" fill="var(--brand-red)"/>
    <polygon points="329,0 337,0 442,491 392,491" fill="var(--wedge-black)"/>
  </svg>

  <div class="brand">
    <span class="brand__mark"></span>
    <span class="brand__name">Macro at Hand</span>
  </div>

  <div class="hero-photo" role="img" aria-label="Black and white photo of bodybuilder Bertil posing on stage with arms outstretched before an audience"></div>

  <p class="motto">Remember,<br>if you fail to plan<br>then you plan to fail</p>

  <div class="visit">
    <p class="visit__lead">Visit us at</p>
    <p class="visit__url">www.macroathand.com.au</p>
    <p class="visit__note">Please visit website for conditions</p>
  </div>

  <ul class="benefits">
    <li class="benefit benefit--1">Live a busy lifestyle? No time to meal prep? We do it for you!</li>
    <li class="benefit benefit--2">Whether you’re bodybuilding or just want truly healthy<span>meals, order from us online</span></li>
    <li class="benefit benefit--3">Grab and Go meals that you can take to work,<span>school...anywhere</span></li>
    <li class="benefit benefit--4">High protein, low fat, low sodium</li>
    <li class="benefit benefit--5">No artificial flavours, colours or preservatives</li>
    <li class="benefit benefit--6">Delivered straight to your door, on the day of<span>your choice</span></li>
    <li class="benefit benefit--7">Affordable prices</li>
  </ul>
</main>
</body>
</html>
```